Velorix Flyer

PROJECT: Digital Flyer for VeloRix

Format
1920 × 1080 px (landscape, optimized for presentations and email)
Deliverables
• PDF
• PNG

About VeloRix
VeloRix is a Dutch B2B software company providing a unified CRM and customer journey platform. We help businesses manage the entire customer lifecycle — from first contact to loyal customer — by centralizing all touchpoints in one system.
What sets us apart:
Extreme ease of use. The system is self-guiding, shows only what's relevant per employee, and requires virtually no training. All channels (email, phone, chat, in-store) come together in one place with automatic task distribution. Built-in AI functions as a smart digital colleague that continuously learns.
Target audience:
Directors and sales managers at B2B companies with multiple customer contact channels.

Goal:
We want to create a flyer that sets us apart from other CRM platform providers. Our aim is to achieve this through simplicity and a professional appearance. The design should reflect our core value: ease of use. The recipient should feel compelled to engage with us — not overwhelmed by information, but intrigued by clarity. Less is more.

Required Text Elements
Headline:
"CRM that adapts to how you work"
Subline:
"Discover how VeloRix simplifies your sales process"
Call-to-action:
"See it in action — book a call"
Contact details:
• hello@velorix.nl
• 023-5718469
• velorix.com

Required Visual Elements
• VeloRix logo (attached)

Design Style
• Modern / Minimalist
• Professional / Business
• Tech / Futuristic
• Clean with plenty of whitespace

Tone of voice:
Clear, positive and customer-focused. Practical and accessible business style aimed at communicating concrete value for users.

Design inspiration — please review these websites:
• orbantal.com
• ravelo.app
• quendo.com
• tirameld.com
• gonwisp.com
What We DON'T Want
• Bold / In-your-face
• Dense / Compact
• Trendy / Experimental
• Childlike / Cheerful
• Playful / Cartoonish
• Busy / Chaotic
Colors
Use the color palette from velorix.com (blues, whites, clean professional tones).
[Exact hex codes used for element on the website:
#344054;
#1a1b1f;
#0254ac
#002249;
#e5edf7;
background-color: #fff; ]
Competitors (for context only — do NOT copy)
• brinvolt.nl
• kelmarin.com
• dortavecrm.com
• wexalunda.com
Budget
$150
Deadline
January 26, 2026

```html
<!DOCTYPE html>
<html lang="en">
<head>
<meta charset="utf-8">
<title>VeloRix Flyer</title>
<link rel="stylesheet" href="https://fonts.googleapis.com/css2?family=Montserrat:wght@500;600;700;800&display=swap">
<style>
  :root {
    --ink: #0a1f44;
    --navy: #002249;
    --brand-blue: #0254ac;
    --sub-blue: #0b4aa6;
    --paper: #f7f7f8;
    --stage: #e9edf3;
    --white: #ffffff;
    --panel-deep: #0a3f99;
    --panel-bright: #1066d8;
  }
  * { margin: 0; padding: 0; box-sizing: border-box; }
  html, body {
    width: 1200px; height: 799px; overflow: hidden;
    background: var(--stage);
    font-family: "Montserrat", Arial, sans-serif;
  }
  .flyer {
    position: absolute; left: 0; top: 62px;
    width: 1200px; height: 675px;
    background: var(--paper);
    overflow: hidden;
  }
  .visual-panel {
    position: absolute; inset: 0;
    width: 1200px; height: 675px;
  }
  .brand {
    position: absolute; left: 74px; top: 32px;
    display: flex; align-items: center; gap: 14px;
  }
  .brand-dot {
    width: 58px; height: 58px; border-radius: 50%;
    background: var(--navy);
  }
  .brand-name {
    font-size: 38px; font-weight: 700; color: var(--navy);
    letter-spacing: 0.2px;
  }
  .headline {
    position: absolute; left: 72px; top: 134px;
    font-size: 55px; line-height: 56px; font-weight: 800;
    color: var(--ink); letter-spacing: 0.3px;
  }
  .subline {
    position: absolute; left: 73px; top: 318px;
    font-size: 25px; line-height: 34px; font-weight: 500;
    color: var(--sub-blue);
  }
  .cta {
    position: absolute; left: 73px; top: 413px;
    width: 436px; height: 53px; border-radius: 27px;
    background: linear-gradient(90deg, #0b52ad 0%, #083a83 55%, #061f4b 100%);
    color: var(--white);
    font-size: 20px; font-weight: 700; letter-spacing: 0.2px;
    display: flex; align-items: center; justify-content: center;
    text-transform: uppercase;
  }
  .contacts {
    position: absolute; left: 78px; top: 500px;
    list-style: none;
  }
  .contact {
    display: flex; align-items: center; height: 41px;
    font-size: 25px; font-weight: 500; color: var(--ink);
  }
  .contact svg { width: 24px; height: 24px; margin-right: 19px; flex: none; }
</style>
</head>
<body>
  <main class="flyer">
    <svg class="visual-panel" viewBox="0 0 1200 675" role="img" aria-label="Blue tech photo: hand holding a phone with a glowing CRM hub surrounded by customer and channel icons">
      <defs>
        <linearGradient id="panelFill" x1="0" y1="1" x2="1" y2="0">
          <stop offset="0" stop-color="#0a4aa3"/>
          <stop offset="0.45" stop-color="#0b52b5"/>
          <stop offset="1" stop-color="#0a3a92"/>
        </linearGradient>
        <radialGradient id="panelGlow" cx="0.8" cy="0.46" r="0.35">
          <stop offset="0" stop-color="#1a7cf0" stop-opacity="0.85"/>
          <stop offset="1" stop-color="#1a7cf0" stop-opacity="0"/>
        </radialGradient>
      </defs>
      <polygon points="992,0 1200,0 1200,675 468,675" fill="url(#panelFill)"/>
      <polygon points="992,0 1200,0 1200,675 468,675" fill="url(#panelGlow)"/>
      <line x1="1200" y1="48" x2="1160" y2="98" stroke="var(--white)" stroke-width="8" stroke-linecap="round"/>
      <line x1="574" y1="628" x2="534" y2="675" stroke="var(--white)" stroke-width="8" stroke-linecap="round"/>
    </svg>

    <div class="brand">
      <span class="brand-dot"></span>
      <span class="brand-name">VeloRix</span>
    </div>

    <h1 class="headline">CRM that adapts<br>to how you work</h1>

    <p class="subline">Discover how VeloRix<br>simplifies your sales process</p>

    <div class="cta">See it in action — book a call</div>

    <ul class="contacts">
      <li class="contact">
        <svg viewBox="0 0 24 24" aria-hidden="true"><rect x="1" y="5" width="22" height="15" rx="2" fill="var(--ink)"/><path d="M2 6l10 7 10-7" fill="none" stroke="var(--paper)" stroke-width="1.8"/></svg>
        hello@velorix.nl
      </li>
      <li class="contact">
        <svg viewBox="0 0 24 24" aria-hidden="true"><path d="M6.6 2.5l3 3.4-1.9 2.4c1.2 2.7 3.3 4.8 6 6l2.4-1.9 3.4 3-1.8 3.3c-7.5-.4-13.2-6.1-13.6-13.6z" fill="var(--ink)"/><path d="M14 3.5a7 7 0 0 1 6.5 6.5M14 6.8a3.8 3.8 0 0 1 3.2 3.2" fill="none" stroke="var(--ink)" stroke-width="1.6" stroke-linecap="round"/></svg>
        023-5718469
      </li>
      <li class="contact">
        <svg viewBox="0 0 24 24" aria-hidden="true"><circle cx="11" cy="11" r="9" fill="none" stroke="var(--ink)" stroke-width="1.8"/><ellipse cx="11" cy="11" rx="4" ry="9" fill="none" stroke="var(--ink)" stroke-width="1.5"/><path d="M2 11h18M3.5 6.5h15M3.5 15.5h15" stroke="var(--ink)" stroke-width="1.4"/><path d="M14 14l8 3-3.5 1.2L17 22z" fill="var(--ink)" stroke="var(--paper)" stroke-width="1"/></svg>
        velorix.com
      </li>
    </ul>
  </main>
</body>
</html>
```